Business Card Design Project for an English Teacher

I need a business card design for my new job.
I'd like to start teaching English as a freelance.
My students will be children, teenager, and adults, who don't like or hesitate to study English and I would like to open a door to the new world for them.

I'd like to put the information below;
[right side]
1. name
2. mail address
3. mobile number
4. website or facebook page

[back]
1.my message: Feel free at asking me anything about my classes

2.lesson list such as:
price: 3150 yen ~

calsses:
kids class( mum& dad can join) ... 30 minutes / 45 minutes
students (over age 13).... 60minutes / 90 minutes
Adult (over age 19) .... 60 minutes / 90 minutes

3. I'll have both Web Lesson and Face to Face Lesson

4. Free trial lesson

Target Market(s)

My students will be children, teenager, and adults, who don't like or hesitate to study English

Industry/Entity Type

Business

Requirements
Must have
• designed both side

```html
<!DOCTYPE html>
<html lang="en">
<head>
<meta charset="utf-8">
<title>English Lessons – Card Back</title>
<link rel="stylesheet" href="https://fonts.googleapis.com/css2?family=Cabin:wght@400;700&family=PT+Sans&display=swap">
<style>
  :root {
    --flag-light: #dde5ef;
    --flag-mid: #a6b6cc;
    --flag-deep: #7a8da8;
    --band-orange: #f7981d;
    --band-shadow: rgba(90, 50, 0, 0.45);
    --paper: #ffffff;
    --ink: #111111;
    --on-orange: #ffffff;
  }
  * { margin: 0; padding: 0; box-sizing: border-box; }
  html, body { width: 1200px; height: 695px; overflow: hidden; background: var(--paper); }
  .card {
    position: relative;
    width: 1200px;
    height: 695px;
    overflow: hidden;
    background: var(--paper);
  }
  .flag-photo {
    position: absolute;
    left: 0; top: 0;
    width: 1200px; height: 580px;
    background:
      radial-gradient(ellipse 380px 160px at 200px 120px, rgba(255,255,255,0.55), transparent 70%),
      radial-gradient(ellipse 420px 200px at 700px 60px, rgba(255,255,255,0.45), transparent 70%),
      linear-gradient(160deg, var(--flag-light) 0%, var(--flag-mid) 45%, var(--flag-deep) 100%);
  }
  .swoosh {
    position: absolute;
    left: 0; top: 0;
    width: 1200px; height: 695px;
  }
  .message {
    position: absolute;
    right: 50px;
    top: 72px;
    text-align: right;
    font-family: "PT Sans", sans-serif;
    font-size: 45px;
    line-height: 58px;
    letter-spacing: 3px;
    color: var(--ink);
  }
  .offer {
    position: absolute;
    right: 50px;
    top: 291px;
    text-align: right;
    font-family: "Cabin", sans-serif;
    font-size: 46px;
    line-height: 54px;
    color: var(--on-orange);
  }
  .classes {
    position: absolute;
    left: 332px;
    top: 448px;
    width: 818px;
    font-family: "Cabin", sans-serif;
    color: var(--ink);
  }
  .classes-title {
    text-align: right;
    font-size: 37px;
    font-weight: 700;
    line-height: 42px;
    padding-bottom: 1px;
    border-bottom: 4px solid var(--ink);
  }
  .class-list { list-style: none; margin-top: 8px; }
  .class-row {
    display: flex;
    justify-content: space-between;
    font-size: 31px;
    line-height: 48px;
  }
</style>
</head>
<body>
  <main class="card">
    <div class="flag-photo" role="img" aria-label="Photo of a waving British flag in soft pale blue tones"></div>

    <svg class="swoosh" viewBox="0 0 1200 695" aria-hidden="true">
      <defs>
        <filter id="edge-shadow" x="-5%" y="-20%" width="110%" height="140%">
          <feGaussianBlur stdDeviation="6"/>
        </filter>
      </defs>
      <path d="M0,414 C380,326 780,270 1200,258 L1200,695 L0,695 Z" fill="var(--band-shadow)" filter="url(#edge-shadow)" transform="translate(0,6)"/>
      <path d="M0,410 C380,322 780,266 1200,256 L1200,695 L0,695 Z" fill="var(--band-orange)"/>
      <path d="M0,556 C380,455 780,400 1200,392 L1200,695 L0,695 Z" fill="var(--paper)"/>
    </svg>

    <p class="message">Feel free at asking me anything<br>about my classes</p>

    <p class="offer">Free trial lesson<br>Both Web Lesson and Face to Face Lesson</p>

    <section class="classes">
      <h2 class="classes-title">classes</h2>
      <ul class="class-list">
        <li class="class-row"><span>kids class( mum&amp; dad can join)</span><span>30 minutes / 45 minutes</span></li>
        <li class="class-row"><span>students (over age 13)</span><span>60minutes / 90 minutes</span></li>
        <li class="class-row"><span>Adult (over age 19)</span><span>60 minutes / 90 minutes</span></li>
      </ul>
    </section>
  </main>
</body>
</html>
```